Business Card Design

We are looking for a double sided business card.

On one side would be our logo

On the Other Side

Martin Kolby
Sales and Marketing

Phone/Text Logo and 530-418-2763
Email Logo and info@plumvalepets.com
Website Logo and www.plumvalepets.com
Facebook Logo and plumvale pets
Instagram Logo and plumvale_pets

Target Market(s)

Pet owners

Contact Information for Business Card

In project description

Requirements
Must have
• Logo

```html
<!DOCTYPE html>
<html lang="en">
<head>
<meta charset="utf-8">
<title>Plumvale Pets – Business Card</title>
<link href="https://fonts.googleapis.com/css2?family=Roboto:wght@400;500;700;900&display=swap" rel="stylesheet">
<style>
  :root {
    --stage: #1b1b1d;
    --card-dark: #2a2a2c;
    --card-dark-deep: #232325;
    --emboss: #3d3d40;
    --white: #ffffff;
    --ink: #262628;
    --orange: #f7941d;
    --orange-deep: #f26522;
    --gold: #f5c400;
    --silver: #d9d9db;
    --text-light: #f2f2f2;
  }
  * { box-sizing: border-box; margin: 0; padding: 0; }
  html, body {
    width: 1200px; height: 840px; overflow: hidden;
    background: var(--stage);
    font-family: "Roboto", Arial, sans-serif;
  }
  .canvas { position: relative; width: 1200px; height: 840px; }

  .card {
    position: absolute;
    width: 640px; height: 366px;
    border-radius: 24px;
    overflow: hidden;
    border-bottom: 4px solid var(--gold);
    border-left: 3px solid var(--gold);
  }

  /* Logo side */
  .card-back { left: 120px; top: 40px; background: var(--card-dark); }
  .back-wordmark {
    position: absolute; left: 0; right: 0; top: 120px;
    text-align: center;
    font-weight: 900; font-size: 64px; letter-spacing: 1px;
    color: var(--emboss);
  }
  .back-url {
    position: absolute; left: 0; right: 0; bottom: 34px;
    text-align: center;
    font-weight: 700; font-size: 16px; letter-spacing: 6px;
    color: var(--orange);
    text-transform: uppercase;
  }

  /* Contact side */
  .card-front { left: 440px; top: 434px; background: var(--white); }
  .front-bg { position: absolute; inset: 0; }
  .monogram-area {
    position: absolute; left: 28px; top: 34px;
    width: 360px; height: 150px;
    border-radius: 14px;
    background: linear-gradient(100deg, var(--silver) 0%, #eeeeee 40%, var(--orange) 75%, var(--orange-deep) 100%);
  }
  .identity {
    position: absolute; right: 34px; top: 30px;
    text-align: right;
  }
  .wordmark {
    font-weight: 900; font-size: 34px; color: var(--ink);
    line-height: 1;
  }
  .person-name {
    margin-top: 26px;
    font-weight: 700; font-size: 24px; color: var(--orange);
    text-transform: uppercase; line-height: 1.1;
  }
  .person-role {
    font-weight: 400; font-size: 17px; color: var(--ink);
  }
  .contacts {
    position: absolute; left: 40px; top: 226px;
    list-style: none;
  }
  .contacts li, .contacts-side li {
    display: flex; align-items: center; gap: 10px;
    height: 24px;
    font-size: 17px; color: var(--text-light);
  }
  .contacts-side {
    position: absolute; left: 360px; top: 226px;
    list-style: none;
  }
  .icon { width: 16px; height: 16px; flex: none; }
  .icon-square { width: 14px; height: 14px; background: var(--orange); border-radius: 2px; flex: none; }
  .icon-circle { width: 14px; height: 14px; background: var(--orange); border-radius: 50%; flex: none; }
</style>
</head>
<body>
<main class="canvas">

  <section class="card card-back" aria-label="Logo side of business card">
    <div class="back-wordmark">Plumvale Pets</div>
    <div class="back-url">www.plumvalepets.com</div>
  </section>

  <section class="card card-front" aria-label="Contact side of business card">
    <svg class="front-bg" width="640" height="366" viewBox="0 0 640 366" aria-hidden="true">
      <path d="M0 215 C 140 200, 260 240, 380 200 S 560 140, 640 150 L 640 366 L 0 366 Z" fill="var(--card-dark)"/>
    </svg>

    <div class="monogram-area" role="img" aria-label="Large brand monogram with flowing helix decoration in silver and orange"></div>

    <div class="identity">
      <div class="wordmark">Plumvale Pets</div>
      <div class="person-name">Martin Kolby</div>
      <div class="person-role">Sales and Marketing</div>
    </div>

    <ul class="contacts">
      <li>
        <svg class="icon" viewBox="0 0 16 16" aria-hidden="true"><path d="M3 1h3l1 4-2 1a9 9 0 0 0 5 5l1-2 4 1v3a2 2 0 0 1-2 2A13 13 0 0 1 1 3a2 2 0 0 1 2-2z" fill="var(--orange)"/></svg>
        530-418-2763
      </li>
      <li>
        <svg class="icon" viewBox="0 0 16 16" aria-hidden="true"><rect x="1" y="3" width="14" height="10" rx="1.5" fill="var(--orange)"/><path d="M1.5 4 8 9l6.5-5" stroke="var(--card-dark)" stroke-width="1.4" fill="none"/></svg>
        info@plumvalepets.com
      </li>
      <li>
        <svg class="icon" viewBox="0 0 16 16" aria-hidden="true"><circle cx="8" cy="8" r="7" fill="var(--orange)"/><path d="M1 8h14M8 1c-3 3-3 11 0 14M8 1c3 3 3 11 0 14" stroke="var(--card-dark)" stroke-width="1.1" fill="none"/></svg>
        www.plumvalepets.com
      </li>
      <li>
        <span class="icon-square" aria-hidden="true"></span>
        plumvale pets
      </li>
    </ul>
    <ul class="contacts-side">
      <li>
        <span class="icon-circle" aria-hidden="true"></span>
        plumvale_pets
      </li>
    </ul>
  </section>

</main>
</body>
</html>
```